Business card design needed

I need a business card design for a new online retail business based in Australia. I am unsure of the exact content of what I will be selling but it will be probably women's clothing, accessories, gym wear, gifts and maybe homeware linen. I am wanting a classy design that portrays the image of class/style/upmarket.

Target Market(s)

predominantely women - 20-50 age group

Industry/Entity Type

Retail

Contact Information for Business Card

Purely Lustre
Karen Whitlow
Director
ABN 73215548906
17 Harcourt Lane Dunmore Ridge NSW 2291
ph: +61 427 390 845
sales@purelylustre.com.au

Logo Text

I am open for suggestions here

Requirements
Must have
• The design must be both sides of the card

```html
<!DOCTYPE html>
<html lang="en">
<head>
<meta charset="utf-8">
<title>Purely Lustre — Business Card</title>
<link rel="stylesheet" href="https://fonts.googleapis.com/css2?family=Questrial&display=swap">
<style>
  :root {
    --page-bg: #2b2b2b;
    --pink-deep: #c8108a;
    --pink-mid: #e0329e;
    --pink-glow: #ff62b4;
    --white: #ffffff;
    --bevel: #d2d2d2;
    --bevel-shade: #b9b9b9;
    --brand-pink: #d01f8d;
  }
  * { box-sizing: border-box; margin: 0; padding: 0; }
  html, body {
    width: 1200px;
    height: 1000px;
    overflow: hidden;
    background: var(--page-bg);
    font-family: "Questrial", "Century Gothic", sans-serif;
  }
  .sheet {
    width: 1200px;
    height: 1000px;
    display: flex;
    flex-direction: column;
    align-items: center;
    justify-content: center;
    gap: 30px;
  }
  .card {
    position: relative;
    width: 800px;
    height: 457px;
    overflow: hidden;
    box-shadow: 0 8px 24px rgba(0,0,0,0.45);
  }
  .card__art {
    position: absolute;
    inset: 0;
    width: 100%;
    height: 100%;
  }
  .brand-name {
    position: absolute;
    left: 80px;
    top: 90px;
    font-size: 60px;
    color: var(--brand-pink);
    letter-spacing: 1px;
    white-space: nowrap;
  }
  .holder {
    position: absolute;
    left: 470px;
    top: 322px;
    color: var(--white);
  }
  .holder__name {
    font-size: 34px;
    letter-spacing: 0.5px;
    white-space: nowrap;
  }
  .holder__role {
    font-size: 18px;
    margin-top: 2px;
  }
  .contact {
    position: absolute;
    left: 400px;
    top: 326px;
    list-style: none;
    color: var(--white);
    font-size: 14px;
    line-height: 26px;
    letter-spacing: 0.5px;
  }
  .contact__item {
    display: flex;
    align-items: center;
    gap: 10px;
    white-space: nowrap;
  }
  .contact__icon {
    width: 17px;
    height: 17px;
    flex: none;
  }
</style>
</head>
<body>
<main class="sheet">

  <section class="card card--front" aria-label="Business card front">
    <svg class="card__art" viewBox="0 0 800 457" preserveAspectRatio="none">
      <defs>
        <radialGradient id="front-pink" cx="78%" cy="62%" r="75%">
          <stop offset="0" stop-color="#ff62b4"/>
          <stop offset="0.5" stop-color="#e0329e"/>
          <stop offset="1" stop-color="#c8108a"/>
        </radialGradient>
        <radialGradient id="front-feather" cx="50%" cy="50%" r="50%">
          <stop offset="0" stop-color="#ffffff" stop-opacity="0.45"/>
          <stop offset="1" stop-color="#ffffff" stop-opacity="0"/>
        </radialGradient>
        <linearGradient id="front-bevel" x1="0" y1="0" x2="1" y2="1">
          <stop offset="0" stop-color="#d2d2d2"/>
          <stop offset="1" stop-color="#b9b9b9"/>
        </linearGradient>
      </defs>
      <rect class="card__field" width="800" height="457" fill="url(#front-pink)"/>
      <path class="card__shield-bevel" d="M0,0 H570 C620,100 620,200 580,255 C525,315 390,320 0,282 Z" fill="url(#front-bevel)"/>
      <path class="card__shield" d="M0,0 H540 C585,90 590,180 555,235 C505,290 380,295 0,258 Z" fill="#ffffff"/>
      <ellipse class="card__feather" role="img" aria-label="Soft feather sparkle decoration" cx="560" cy="360" rx="90" ry="70" fill="url(#front-feather)"/>
    </svg>
    <div class="brand-name">Purely Lustre</div>
    <div class="holder">
      <div class="holder__name">Karen Whitlow</div>
      <div class="holder__role">Director</div>
    </div>
  </section>

  <section class="card card--back" aria-label="Business card back">
    <svg class="card__art" viewBox="0 0 800 457" preserveAspectRatio="none">
      <defs>
        <radialGradient id="back-pink" cx="72%" cy="68%" r="75%">
          <stop offset="0" stop-color="#ff62b4"/>
          <stop offset="0.5" stop-color="#e0329e"/>
          <stop offset="1" stop-color="#c8108a"/>
        </radialGradient>
        <radialGradient id="back-feather" cx="50%" cy="50%" r="50%">
          <stop offset="0" stop-color="#ffffff" stop-opacity="0.4"/>
          <stop offset="1" stop-color="#ffffff" stop-opacity="0"/>
        </radialGradient>
        <linearGradient id="back-bevel" x1="0" y1="0" x2="1" y2="1">
          <stop offset="0" stop-color="#d2d2d2"/>
          <stop offset="1" stop-color="#b9b9b9"/>
        </linearGradient>
      </defs>
      <rect class="card__field" width="800" height="457" fill="url(#back-pink)"/>
      <path class="card__shield-bevel" d="M0,0 H570 C620,100 620,200 580,255 C525,315 390,320 0,282 Z" fill="url(#back-bevel)"/>
      <path class="card__shield" d="M0,0 H540 C585,90 590,180 555,235 C505,290 380,295 0,258 Z" fill="#ffffff"/>
      <ellipse class="card__feather" role="img" aria-label="Soft feather sparkle decoration" cx="540" cy="370" rx="95" ry="70" fill="url(#back-feather)"/>
    </svg>
    <div class="brand-name">Purely Lustre</div>
    <ul class="contact">
      <li class="contact__item">
        <svg class="contact__icon" viewBox="0 0 18 18"><rect x="1" y="1" width="16" height="16" rx="3" fill="#fff"/><rect x="5" y="4" width="8" height="10" rx="1" fill="none" stroke="#c8108a" stroke-width="1.4"/><path d="M7 7h4M7 9.5h4M7 12h2" stroke="#c8108a" stroke-width="1.2"/></svg>
        ABN 73215548906
      </li>
      <li class="contact__item">
        <svg class="contact__icon" viewBox="0 0 18 18"><rect x="1" y="1" width="16" height="16" rx="3" fill="#fff"/><path d="M5.5 4.5l2 0 1 3-1.3 1c.7 1.4 1.6 2.3 3 3l1-1.3 3 1v2c0 .6-.5 1-1 1C8.5 14 4 9.5 4.5 5.5c0-.6.4-1 1-1z" fill="#c8108a"/></svg>
        +61 427 390 845
      </li>
      <li class="contact__item">
        <svg class="contact__icon" viewBox="0 0 18 18"><rect x="1" y="1" width="16" height="16" rx="3" fill="#fff"/><path d="M9 3.5a3.5 3.5 0 0 1 3.5 3.5c0 2.6-3.5 7-3.5 7S5.5 9.6 5.5 7A3.5 3.5 0 0 1 9 3.5z" fill="#c8108a"/><circle cx="9" cy="7" r="1.3" fill="#fff"/></svg>
        17 Harcourt Lane Dunmore Ridge NSW 2291
      </li>
      <li class="contact__item">
        <svg class="contact__icon" viewBox="0 0 18 18"><rect x="1" y="1" width="16" height="16" rx="3" fill="#fff"/><rect x="4" y="5.5" width="10" height="7" rx="1" fill="none" stroke="#c8108a" stroke-width="1.4"/><path d="M4.5 6l4.5 3.5L13.5 6" fill="none" stroke="#c8108a" stroke-width="1.3"/></svg>
        sales@purelylustre.com.au
      </li>
    </ul>
  </section>

</main>
</body>
</html>
```